Buchcover für ein Glücksbuch
Zielgruppe
Ich brauche ein Cover für mein Glücksbuch, es soll möglichst viele interessierte Leser ansprechen und zum Kauf des Buches animieren.
Mein Glücksbuch ist für jeden gedacht, der auch im Alltag in kleinen Dingen sein Glück sucht, es muss nicht immer das große Glück sein und auch Geld allein macht nicht glücklich. Es soll den Leser dazu bringen, das Glück in sich selbt zu finden. Es enthält Anleitungen und Tipps und eine Bonus-Mediation.
Aufgabenstellung
Der Titel des Buches lautet: 'Pfade zur Freude mit 12 Herzensfunken'
Untertitel: 'Heiter und gelassen jeden Tag mit Ideen und Übungen'
'Mit Bonus-Meditation'
Autorin (Pseudonym): Britta Wolder

```html
<!DOCTYPE html>
<html lang="de">
<head>
<meta charset="utf-8">
<title>Pfade zur Freude mit 12 Herzensfunken – Buchcover</title>
<link rel="stylesheet" href="https://fonts.googleapis.com/css2?family=Alegreya:wght@400;500&family=Oswald:wght@500&family=Poppins:wght@300&display=swap">
<style>
  :root{
    --violet-deep:#6a3a8e;
    --violet-badge:#5a3383;
    --violet-mid:#8a62b8;
    --violet-light:#b9a3da;
    --lilac-haze:#ddd2ee;
    --white:#ffffff;
    --photo-grey:#c9c8c4;
    --bug-red:#d8282a;
  }
  *{margin:0;padding:0;box-sizing:border-box}
  html,body{width:1200px;height:833px;overflow:hidden;background:var(--white)}
  .cover{position:relative;width:1200px;height:833px;overflow:hidden}

  .back-photo,.front-photo{position:absolute;top:0;height:833px}
  .back-photo{left:0;width:557px;
    background:
      radial-gradient(ellipse 260px 160px at 200px 40px,var(--lilac-haze),transparent 70%),
      radial-gradient(ellipse 200px 260px at 470px 470px,var(--violet-light),transparent 70%),
      radial-gradient(ellipse 300px 200px at 100px 760px,var(--violet-light),transparent 70%),
      linear-gradient(160deg,var(--violet-mid),#7b55ad 55%,#9678c6);}
  .front-photo{left:620px;width:580px;
    background:
      radial-gradient(ellipse 110px 130px at 330px 440px,rgba(216,40,42,.75),transparent 70%),
      radial-gradient(ellipse 240px 140px at 260px 40px,var(--lilac-haze),transparent 70%),
      radial-gradient(ellipse 200px 260px at 60px 520px,var(--violet-light),transparent 70%),
      linear-gradient(165deg,#8b66bb,#7a54ab 50%,#9577c4);}

  .author-portrait{position:absolute;left:42px;top:99px;width:170px;height:215px;
    background:linear-gradient(180deg,var(--photo-grey),#1f6b3e 120%);z-index:2}

  .blurb{position:absolute;left:115px;top:127px;width:311px;height:509px;
    background:var(--violet-deep);color:var(--white);
    font:300 10.2px/15.65px "Poppins",sans-serif;letter-spacing:-0.25px}
  .blurb p{position:absolute;right:19px}
  .blurb .p1{left:113px;top:62px}
  .blurb .p2{left:24px;top:205px}
  .blurb .p3{left:24px;top:318px}
  .blurb .line{display:block;white-space:nowrap;text-align:justify;text-align-last:justify}
  .blurb .line.end{text-align-last:left}

  .spine{position:absolute;left:557px;top:0;width:63px;height:833px;background:var(--violet-deep)}
  .spine-title{position:absolute;left:31px;top:399px;white-space:nowrap;
    transform:translate(-50%,-50%) rotate(-90deg);
    font:400 39px/1 "Alegreya",serif;color:var(--white)}
  .spine-author{position:absolute;left:0;width:63px;top:764px;text-align:center;
    font:500 22px/28px "Oswald",sans-serif;color:var(--white)}

  .front-title{position:absolute;right:86px;top:17px;text-align:right;
    font:400 96px/104px "Alegreya",serif;color:var(--white)}
  .title-line{display:block}
  .title-count{position:absolute;left:644px;top:200px;white-space:nowrap;color:var(--white);font-family:"Alegreya",serif}
  .title-count .mit{font-size:42px}
  .title-count .num{font-size:126px;line-height:1;margin:0 6px}
  .title-count .word{font-size:43px}
  .front-author{position:absolute;right:62px;top:314px;
    font:500 40px/1 "Oswald",sans-serif;color:var(--white)}
  .subtitle{position:absolute;left:630px;width:565px;top:732px;text-align:center;
    font:400 34px/37px "Alegreya",serif;color:var(--white)}

  .bonus-badge{position:absolute;left:1051px;top:540px;width:152px;height:152px}
</style>
</head>
<body>
<main class="cover">
  <div class="back-photo" role="img" aria-label="Weichgezeichnete lila Fliederblüten als Hintergrund"></div>
  <div class="author-portrait" role="img" aria-label="Porträtfoto der Autorin"></div>
  <section class="blurb">
    <p class="p1">
      <span class="line">In den 25 Jahren meiner selbstän-</span>
      <span class="line">digen Arbeit als Hebamme, habe</span>
      <span class="line">ich viele Familien im Wochenbett</span>
      <span class="line">betreut und dabei einen reichen</span>
      <span class="line">Erfahrungsschatz gesammelt.</span>
      <span class="line">Meine häufigsten Kunden waren</span>
      <span class="line">natürlich Familien, die das erste</span>
      <span class="line end">Kind bekommen haben.</span>
    </p>
    <p class="p2">
      <span class="line">Dies war zu der Zeit, als gerade der Krankenhaus-</span>
      <span class="line">aufenthalt nach einer Spontangeburt von zehn</span>
      <span class="line">auf sieben Tage gekürzt worden war. Die Kran-</span>
      <span class="line">kenkasse bezahlte im Anschluss daran vier Tage</span>
      <span class="line">Hebammen- Betreuung. Wenn die Familie diver-</span>
      <span class="line">se schwierige Themenfelder hatte, übernahm die</span>
      <span class="line end">Kasse die Kosten auch länger.</span>
    </p>
    <p class="p3">
      <span class="line">Da ich meinen Beruf liebte, nahm ich mir für den</span>
      <span class="line">Wochenbettbesuch auch immer genügend Zeit.</span>
      <span class="line">Meist war eine Stunde nötig, manchmal jedoch</span>
      <span class="line">waren so viele Fragen oder Irritationen (Unklar-</span>
      <span class="line">heiten), daß ich länger blieb. Auf die frisch geba-</span>
      <span class="line">ckenen Eltern kommen unzählige unbekannte Si-</span>
      <span class="line">tuationen zu, die total verunsichern können. Auch</span>
      <span class="line">bei sehr einfühlsamer Betreuung im Krankenhaus</span>
      <span class="line">stellen sich viele Fragen erst zu Hause. Nämlich</span>
      <span class="line end">dann, wenn der Alltag mit dem Baby beginnt.</span>
    </p>
  </section>

  <div class="spine">
    <div class="spine-title">Pfade zur Freude mit 12 Herzens- funken</div>
    <div class="spine-author">Britta<br>Wolder</div>
  </div>

  <div class="front-photo" role="img" aria-label="Marienkäfer auf lila Fliederblüte, weichgezeichnet"></div>
  <h1 class="front-title"><span class="title-line">Pfade zur</span><span class="title-line">Freude</span></h1>
  <div class="title-count"><span class="mit">mit</span><span class="num">12</span><span class="word">Herzensfunken</span></div>
  <div class="front-author">Britta Wolder</div>
  <p class="subtitle">Heiter und gelassen jeden Tag mit<br>Ideen und Übungen</p>

  <svg class="bonus-badge" viewBox="0 0 152 152" aria-label="Mit Bonus-Meditation">
    <defs><path id="badge-arc" d="M28 50 A54 54 0 1 0 124 50"/></defs>
    <circle cx="76" cy="76" r="74" fill="var(--violet-badge)"/>
    <circle cx="76" cy="76" r="20" fill="var(--bug-red)" role="img" aria-label="Kleiner Marienkäfer"/>
    <text fill="var(--white)" font-family="Oswald, sans-serif" font-weight="500" font-size="22" letter-spacing="1">
      <textPath href="#badge-arc" startOffset="50%" text-anchor="middle">Mit Bonus-Meditation</textPath>
    </text>
  </svg>
</main>
</body>
</html>
```